Power Crest job sheet re-desgin

i require a very corporate detail job sheet for my business. it needs to have all that is listened on the one i have attached and it also needs to have the maintenance JSA and the test report. i have attached my logo and that also needs to be used in all. i require it to be on a A4 sheet layout it can be more then one page.

Target Market(s)

no target market as of yet

Industry/Entity Type

Electrical

Requirements
Must have
• it must have all that is on all sheets that i have uploaded. Apart from the electrical test sheet it has my old company name ridgeline volt that needs to be removed. It also needs to be in a word doc so I am able to print the sheets off.

```html
<!DOCTYPE html>
<html lang="en">
<head>
<meta charset="utf-8">
<title>Power Crest – Job Sheet, Test Report, Work Method Statement</title>
<link href="https://fonts.googleapis.com/css2?family=Open+Sans:wght@400;600;700&display=swap" rel="stylesheet">
<style>
:root{
  --teal:#1a9cc4;
  --teal-dark:#12809f;
  --slate:#5f6b70;
  --ink:#333b3e;
  --row-a:#e8e5e5;
  --row-b:#f4f3f3;
  --paper:#ffffff;
  --backdrop:#1f1f1f;
  --rule:#9aa3a6;
}
*{box-sizing:border-box;margin:0;padding:0}
html,body{width:1200px;height:880px;overflow:hidden;background:var(--backdrop)}
body{font-family:"Open Sans",Arial,sans-serif;color:var(--ink)}
.canvas{position:relative;width:1200px;height:880px;overflow:hidden}
.sheet{position:absolute;background:var(--paper);overflow:hidden;box-shadow:0 6px 18px rgba(0,0,0,.5)}
.brand{display:flex;align-items:center;gap:5px;font-weight:700;color:var(--teal);letter-spacing:.5px}
.brand-dot{width:9px;height:9px;border-radius:50%;background:var(--teal)}
.brand-sub{font-size:5px;color:var(--slate);letter-spacing:1px;font-weight:600;display:block}

/* Job sheet */
.job{left:18px;top:150px;width:384px;height:520px}
.job-head{position:relative;height:62px}
.job-head .brand{position:absolute;left:14px;top:26px;font-size:15px}
.job-band{position:absolute;right:0;top:0;width:230px;height:40px;background:linear-gradient(180deg,var(--slate) 0 15%,var(--teal) 15% 85%,var(--slate) 85% 100%)}
.field{font-size:7px;display:flex;align-items:flex-end;gap:4px;height:11px}
.field .line{flex:1;border-bottom:1px solid var(--rule);height:1px}
.job-fields{display:grid;grid-template-columns:1fr 1fr;gap:14px;padding:4px 14px 0}
.job-left .field,.job-right .field{margin-bottom:2px}
.job-boxes{margin-top:6px}
.job-boxes .field{border:1px solid var(--teal);color:var(--teal);font-weight:600;padding:0 4px 1px;height:13px;margin-bottom:2px}
.note-lines .line{border-bottom:1px solid var(--rule);height:11px}
.grid-table{width:100%;border-collapse:collapse;font-size:6.5px;table-layout:fixed}
.grid-table th{background:var(--teal);color:#fff;font-weight:600;height:11px;text-align:center}
.grid-table td{height:10px;border-right:1px solid #fff}
.grid-table tr:nth-child(odd) td{background:var(--row-a)}
.grid-table tr:nth-child(even) td{background:var(--row-b)}
.section-tab{display:inline-block;background:var(--slate);color:#fff;font-size:8px;font-weight:600;padding:1px 18px 1px 8px;clip-path:polygon(0 0,100% 0,88% 100%,0 100%)}
.job-tables{padding:10px 14px 0}
.job-foot-brand{display:flex;justify-content:flex-end;padding:8px 14px 6px}
.job-foot-brand .brand{font-size:11px}
.job-footer{position:absolute;left:0;right:0;bottom:0;height:34px;background:#d9dddf;display:grid;grid-template-columns:1fr 1fr;font-size:6px;color:var(--slate);padding:7px 14px;gap:2px 10px}
.job-footer span{display:flex;align-items:center;gap:4px}

/* Test report */
.test{left:418px;top:18px;width:764px;height:398px;padding:10px 14px}
.sheet-top{display:flex;justify-content:space-between;align-items:flex-start}
.title-band{background:var(--slate);color:#fff;font-size:9px;font-weight:600;padding:2px 26px 2px 8px;clip-path:polygon(0 0,100% 0,94% 100%,0 100%);display:inline-block}
.test .brand{font-size:12px}
.meta{display:grid;grid-template-columns:1fr 1fr;gap:2px 30px;margin-top:4px}
.certify{font-size:6px;line-height:1.35;color:var(--slate);margin:4px 0}
.test-table th{font-size:5.8px;height:24px;line-height:1.15;padding:0 2px;border-right:1px solid #fff}
.test-table td{height:13px}

/* Work method statement */
.wms{left:418px;top:432px;width:764px;height:434px;padding:10px 14px}
.wms .brand{font-size:12px}
.notice{background:var(--teal);color:#fff;font-size:8.5px;font-weight:600;padding:2px 8px;margin-top:6px}
.wms-table{width:100%;border-collapse:collapse;table-layout:fixed;font-size:6.4px}
.wms-table th{background:var(--teal);color:#fff;font-weight:600;font-size:6px;line-height:1.15;height:26px;border-right:1px solid #fff;padding:0 3px}
.wms-table td{height:13px;padding:0 4px;white-space:nowrap;overflow:hidden}
.wms-table tr:nth-child(odd) td{background:var(--row-b)}
.wms-table tr:nth-child(even) td{background:#fff}
.tick{display:inline-block;width:7px;height:7px;border:1px solid var(--slate);vertical-align:middle}
.c{text-align:center}
.strong{font-weight:700}
.wms-foot{font-size:6.6px;margin-top:6px;line-height:1.5}
</style>
</head>
<body>
<main class="canvas">

  <!-- Job sheet -->
  <section class="sheet job">
    <header class="job-head">
      <div class="brand"><span class="brand-dot"></span><span>Power Crest<span class="brand-sub">ELECTRICAL CONTRACTORS</span></span></div>
      <div class="job-band" role="img" aria-label="Decorative header band in slate and teal"></div>
    </header>
    <div class="job-fields">
      <div class="job-left">
        <div class="field">Client:<span class="line"></span></div>
        <div class="field">Phone:<span class="line"></span></div>
        <div class="field">Contact Person:<span class="line"></span></div>
        <div class="job-boxes">
          <div class="field">Job Number:<span class="line"></span></div>
          <div class="field">Status:<span class="line"></span></div>
          <div class="field">Priority:<span class="line"></span></div>
          <div class="field">Due Date:<span class="line"></span></div>
          <div class="field">Complete Date:<span class="line"></span></div>
          <div class="field">Responsible Person:<span class="line"></span></div>
        </div>
      </div>
      <div class="job-right">
        <div class="field">Site:<span class="line"></span></div>
        <div class="field">Contact Person Number:<span class="line"></span></div>
        <div class="field">Job Notes:<span class="line"></span></div>
        <div class="note-lines"><div class="line"></div><div class="line"></div></div>
        <div class="field" style="margin-top:6px">Work Performed:<span class="line"></span></div>
        <div class="note-lines"><div class="line"></div><div class="line"></div><div class="line"></div></div>
      </div>
    </div>
    <div class="job-tables">
      <span class="section-tab">Materials</span>
      <table class="grid-table">
        <colgroup><col style="width:16%"><col style="width:40%"><col><col><col></colgroup>
        <tr><th>Code</th><th>Description</th><th>Unit</th><th>Length</th><th>Qty</th></tr>
        <tr><td></td><td></td><td></td><td></td><td></td></tr>
        <tr><td></td><td></td><td></td><td></td><td></td></tr>
        <tr><td></td><td></td><td></td><td></td><td></td></tr>
        <tr><td></td><td></td><td></td><td></td><td></td></tr>
        <tr><td></td><td></td><td></td><td></td><td></td></tr>
        <tr><td></td><td></td><td></td><td></td><td></td></tr>
      </table>
      <table class="grid-table" style="margin-top:8px">
        <colgroup><col style="width:26%"><col><col><col><col></colgroup>
        <tr><th>Employee</th><th>Date</th><th>Start Time</th><th>Finish Time</th><th>Hours</th></tr>
        <tr><td></td><td></td><td></td><td></td><td></td></tr>
        <tr><td></td><td></td><td></td><td></td><td></td></tr>
        <tr><td></td><td></td><td></td><td></td><td></td></tr>
        <tr><td></td><td></td><td></td><td></td><td></td></tr>
        <tr><td></td><td></td><td></td><td></td><td></td></tr>
        <tr><td></td><td></td><td></td><td></td><td></td></tr>
      </table>
    </div>
    <div class="job-foot-brand"><div class="brand"><span class="brand-dot"></span><span>Power Crest<span class="brand-sub">ELECTRICAL CONTRACTORS</span></span></div></div>
    <footer class="job-footer">
      <span><svg width="6" height="8" viewBox="0 0 6 8" aria-hidden="true"><path d="M3 0a3 3 0 0 1 3 3c0 2-3 5-3 5S0 5 0 3a3 3 0 0 1 3-3z" fill="#5f6b70"/></svg>Sample Street 48, Riverton Australia</span>
      <span><svg width="7" height="7" viewBox="0 0 7 7" aria-hidden="true"><circle cx="3.5" cy="3.5" r="3" fill="none" stroke="#5f6b70"/></svg>www.powercrest.com.au</span>
      <span><svg width="7" height="7" viewBox="0 0 7 7" aria-hidden="true"><path d="M1 0h2l1 2-1 1a4 4 0 0 0 1 1l1-1 2 1v2C4 7 0 3 1 0z" fill="#5f6b70"/></svg>Phone: 123 555 0190</span>
      <span><svg width="8" height="6" viewBox="0 0 8 6" aria-hidden="true"><rect x=".5" y=".5" width="7" height="5" fill="none" stroke="#5f6b70"/><path d="M.5.5 4 3.5 7.5.5" fill="none" stroke="#5f6b70"/></svg>contact@powercrest.com.au</span>
    </footer>
  </section>

  <!-- Electrical test report -->
  <section class="sheet test">
    <div class="sheet-top">
      <span class="title-band">Electrical Test Report</span>
      <div class="brand"><span class="brand-dot"></span><span>Power Crest<span class="brand-sub">ELECTRICAL CONTRACTORS</span></span></div>
    </div>
    <div class="meta">
      <div class="field">Customer Name:<span class="line"></span></div>
      <div class="field">Test Date:<span class="line"></span></div>
      <div class="field">Site Address:<span class="line"></span></div>
      <div class="field">Work Activity / Task:<span class="line"></span></div>
    </div>
    <p class="certify">I certify that the electrical installation, to the extent that it is affected by the electrical work, has been tested to ensure it is electrically safe and is in accordance with the requirements of the wiring rules and any other standard applying to the electrical installation under the Electrical Safety Regulation 2002.</p>
    <div class="meta" style="grid-template-columns:1fr 1fr 1fr;margin:0 0 6px">
      <div class="field">Name:<span class="line"></span></div>
      <div class="field">Signature:<span class="line"></span></div>
      <div class="field">Supervisor:<span class="line"></span></div>
    </div>
    <table class="grid-table test-table">
      <tr><th>Circuit Designation</th><th>Visual Inspection Complete</th><th>Circuit No.</th><th>Protection Size / Type</th><th>Neutral No.</th><th>Cable Size</th><th>Continuity Test (Ohms)</th><th>Insulation Resistance Test (MΩ)</th><th>Polarity Test Connected Correct</th><th>Fault Loop Imp. Test (Ohms)</th><th>RCD Trip Time</th><th>Comments</th></tr>
      <tr><td></td><td></td><td></td><td></td><td></td><td></td><td></td><td></td><td></td><td></td><td></td><td></td></tr>
      <tr><td></td><td></td><td></td><td></td><td></td><td></td><td></td><td></td><td></td><td></td><td></td><td></td></tr>
      <tr><td></td><td></td><td></td><td></td><td></td><td></td><td></td><td></td><td></td><td></td><td></td><td></td></tr>
      <tr><td></td><td></td><td></td><td></td><td></td><td></td><td></td><td></td><td></td><td></td><td></td><td></td></tr>
      <tr><td></td><td></td><td></td><td></td><td></td><td></td><td></td><td></td><td></td><td></td><td></td><td></td></tr>
      <tr><td></td><td></td><td></td><td></td><td></td><td></td><td></td><td></td><td></td><td></td><td></td><td></td></tr>
      <tr><td></td><td></td><td></td><td></td><td></td><td></td><td></td><td></td><td></td><td></td><td></td><td></td></tr>
      <tr><td></td><td></td><td></td><td></td><td></td><td></td><td></td><td></td><td></td><td></td><td></td><td></td></tr>
      <tr><td></td><td></td><td></td><td></td><td></td><td></td><td></td><td></td><td></td><td></td><td></td><td></td></tr>
      <tr><td></td><td></td><td></td><td></td><td></td><td></td><td></td><td></td><td></td><td></td><td></td><td></td></tr>
      <tr><td></td><td></td><td></td><td></td><td></td><td></td><td></td><td></td><td></td><td></td><td></td><td></td></tr>
      <tr><td></td><td></td><td></td><td></td><td></td><td></td><td></td><td></td><td></td><td></td><td></td><td></td></tr>
      <tr><td></td><td></td><td></td><td></td><td></td><td></td><td></td><td></td><td></td><td></td><td></td><td></td></tr>
      <tr><td></td><td></td><td></td><td></td><td></td><td></td><td></td><td></td><td></td><td></td><td></td><td></td></tr>
      <tr><td></td><td></td><td></td><td></td><td></td><td></td><td></td><td></td><td></td><td></td><td></td><td></td></tr>
    </table>
  </section>

  <!-- Work method statement -->
  <section class="sheet wms">
    <div class="sheet-top">
      <span class="title-band">Work Method Statement - Maintenance Works</span>
      <div class="brand"><span class="brand-dot"></span><span>Power Crest<span class="brand-sub">ELECTRICAL CONTRACTORS</span></span></div>
    </div>
    <div class="meta">
      <div class="field">Customer Name:<span class="line"></span></div>
      <div class="field">Date:<span class="line"></span></div>
      <div class="field">Site Address:<span class="line"></span></div>
      <div class="field">Work Activity / Task:<span class="line"></span></div>
      <div class="field">Job Number:<span class="line"></span></div>
      <div class="field">Install Fans:<span class="line"></span></div>
    </div>
    <div class="notice">This WMS must be completed before commencing each job / task</div>
    <table class="wms-table">
      <colgroup><col style="width:22%"><col style="width:4%"><col style="width:16%"><col style="width:4%"><col style="width:9%"><col style="width:27%"><col style="width:4%"><col style="width:14%"></colgroup>
      <tr><th colspan="2">Work Activity<br>Tick jobs to be carried out &amp; any specific that maybe required, list others</th><th colspan="2">Potential Hazard<br>Tick boxes for risks that apply</th><th>Risk H/M/L Circle</th><th colspan="2">Control Measures<br>What you will do to make the job safe in order to lower risk</th><th>Risk After Control Measures Are Put Into Place Circle</th></tr>
      <tr><td>Repair Lights</td><td class="c"><span class="tick"></span></td><td>Eye Injury</td><td class="c"><span class="tick"></span></td><td class="c">H/M/L</td><td>Wear Safety Glasses or Shield</td><td class="c"><span class="tick"></span></td><td class="c">H/M/L</td></tr>
      <tr><td>Repair HWS</td><td class="c"><span class="tick"></span></td><td>Hearing Damage</td><td class="c"><span class="tick"></span></td><td class="c">H/M/L</td><td>Wear ear protection</td><td class="c"><span class="tick"></span></td><td class="c">H/M/L</td></tr>
      <tr><td>Repair Range/Cook Top</td><td class="c"><span class="tick"></span></td><td>Slipping</td><td class="c"><span class="tick"></span></td><td class="c">H/M/L</td><td>Clean area, wear safety boots</td><td class="c"><span class="tick"></span></td><td class="c">H/M/L</td></tr>
      <tr><td>Repair Power Outage</td><td class="c"><span class="tick"></span></td><td>Falling</td><td class="c"><span class="tick"></span></td><td class="c">H/M/L</td><td>3 points of contact on Ladder</td><td class="c"><span class="tick"></span></td><td class="c">H/M/L</td></tr>
      <tr><td>Replace Sweep Fan</td><td class="c"><span class="tick"></span></td><td>Cuts &amp; Abrasions</td><td class="c"><span class="tick"></span></td><td class="c">H/M/L</td><td>Wear PPE</td><td class="c"><span class="tick"></span></td><td class="c">H/M/L</td></tr>
      <tr><td>Replace Dimmer</td><td class="c"><span class="tick"></span></td><td>Dehydration</td><td class="c"><span class="tick"></span></td><td class="c">H/M/L</td><td>Drink plenty of water</td><td class="c"><span class="tick"></span></td><td class="c">H/M/L</td></tr>
      <tr><td>Fix Sensor Light</td><td class="c"><span class="tick"></span></td><td>Sun Exposure</td><td class="c"><span class="tick"></span></td><td class="c">H/M/L</td><td>Apply suncream &amp; wear hat</td><td class="c"><span class="tick"></span></td><td class="c">H/M/L</td></tr>
      <tr><td>Install RCD</td><td class="c"><span class="tick"></span></td><td>Burns</td><td class="c"><span class="tick"></span></td><td class="c">H/M/L</td><td>Shield from sparks, wear PPE</td><td class="c"><span class="tick"></span></td><td class="c">H/M/L</td></tr>
      <tr><td>Install Circuit Breaker</td><td class="c"><span class="tick"></span></td><td>Pinching</td><td class="c"><span class="tick"></span></td><td class="c">H/M/L</td><td>Wear PPE &amp; long sleeves</td><td class="c"><span class="tick"></span></td><td class="c">H/M/L</td></tr>
      <tr><td>Change Power Point</td><td class="c"><span class="tick"></span></td><td>Dust Inhalation</td><td class="c"><span class="tick"></span></td><td class="c">H/M/L</td><td>Wear Dust mask or respirator</td><td class="c"><span class="tick"></span></td><td class="c">H/M/L</td></tr>
      <tr><td>Change Light Switch</td><td class="c"><span class="tick"></span></td><td>Tripping</td><td class="c"><span class="tick"></span></td><td class="c">H/M/L</td><td>Clean work area, wear PPE</td><td class="c"><span class="tick"></span></td><td class="c">H/M/L</td></tr>
      <tr><td>Replace Fan Controller</td><td class="c"><span class="tick"></span></td><td>Skin Irritation</td><td class="c"><span class="tick"></span></td><td class="c">H/M/L</td><td>Wear long sleeves &amp; PPE</td><td class="c"><span class="tick"></span></td><td class="c">H/M/L</td></tr>
      <tr><td>Other (List other Job Steps)</td><td class="c"><span class="tick"></span></td><td class="strong">Electric Shock</td><td class="c"><span class="tick"></span></td><td class="c">H/M/L</td><td class="strong">Isolate Power (No Live Works)</td><td class="c"><span class="tick"></span></td><td class="c">H/M/L</td></tr>
      <tr><td></td><td></td><td>Other (List)</td><td class="c"><span class="tick"></span></td><td class="c">H/M/L</td><td>Other (List)</td><td></td><td class="c">H/M/L</td></tr>
      <tr><td></td><td></td><td>Site Conditions</td><td class="c"><span class="tick"></span></td><td class="c">H/M/L</td><td>Familiarise yourself with the Site &amp; check with Site Personnel</td><td class="c"><span class="tick"></span></td><td class="c">H/M/L</td></tr>
      <tr><td>Inspect Site</td><td class="c"><span class="tick"></span></td><td></td><td></td><td></td><td>&amp; implement further control measures as necessary.</td><td></td><td></td></tr>
    </table>
    <div class="wms-foot">
      <p><span class="strong">Please do not proceed with any works should you feel your safety maybe compromised, contact your supervisor.</span></p>
      <p>I am satisfied with the control measures I have put in place to achieve a safe working environment for myself, the customer, fellow workers and the general public.</p>
      <div class="meta" style="margin-top:2px"><div class="field">Name:<span class="line"></span></div><div class="field">Signature:<span class="line"></span></div></div>
    </div>
  </section>

</main>
</body>
</html>
```